Sympathy Gift Supplier needs packaging designs

We provide sympathy/bereavement gifts such as memorial candles and picture frames for those who recently lost a loved one. We need packaging design for our boxes that will be uplifting and positive, yet elegant.

We have attached our logo in white and black as well as a saying we would like on the box, and what we need on the back panel.
Ignore the black as it was something we were working on for another product.

Target Market(s)

These products will be given as gifts to people who lost a loved one as remembrance.

Requirements
Must have
• Back panel details (provided)
Memorial quote (provided)
Must be appropriate for this type of product

```html
<!DOCTYPE html>
<html lang="en">
<head>
<meta charset="utf-8">
<title>Memorial Candle Card – Front and Back</title>
<link href="https://fonts.googleapis.com/css2?family=Dancing+Script:wght@600&family=Quicksand:wght@400;500&display=swap" rel="stylesheet">
<style>
  :root {
    --backdrop: #aba9ab;
    --marble-white: #f1f1f1;
    --paper: #f7f7f6;
    --ink: #161616;
    --frame-line: #bdbdbd;
    --bloom-plum: #7a6670;
    --bloom-sage: #9aa59c;
    --bloom-ivory: #e4e1de;
    --brand: #5b2a86;
  }
  * { margin: 0; padding: 0; box-sizing: border-box; }
  html, body { width: 1200px; height: 960px; overflow: hidden; }
  body { background: var(--backdrop); position: relative; font-family: "Quicksand", sans-serif; }

  .card { position: absolute; top: 83px; height: 794px; overflow: hidden; }
  .card--front { left: 55px; width: 529px; background: var(--marble-white); }
  .card--back {
    left: 614px; width: 531px;
    background: linear-gradient(160deg, #f6f6f6 0%, #efefef 55%, #e9e9e9 100%);
    text-align: center; color: var(--ink);
  }

  .split { position: absolute; inset: 0; }

  .floral-area {
    position: absolute; left: 40px; top: 80px; width: 450px; height: 630px;
    border-radius: 32px;
    background: linear-gradient(160deg, var(--bloom-ivory) 0%, var(--bloom-sage) 50%, var(--bloom-plum) 100%);
  }

  .quote-frame {
    position: absolute; left: 99px; top: 182px; width: 328px; height: 427px;
    border: 1px solid var(--frame-line); outline: 1px solid var(--frame-line); outline-offset: -4px;
  }
  .quote-panel {
    position: absolute; left: 118px; top: 209px; width: 288px; height: 378px;
    background: var(--paper);
    display: flex; align-items: center; justify-content: center;
  }
  .quote {
    font-family: "Dancing Script", cursive; font-weight: 600;
    font-size: 28px; line-height: 38.4px; text-align: center; color: var(--ink);
  }

  .notice { position: absolute; left: 0; width: 100%; }
  .notice--warning { top: 195px; }
  .notice--burning { top: 371px; }
  .notice__title {
    font-size: 16.5px; font-weight: 500; letter-spacing: 3.5px; line-height: 30px;
  }
  .notice__body {
    font-size: 18.5px; font-weight: 400; line-height: 33.6px;
    white-space: nowrap; margin-top: 2px;
  }

  .brand {
    position: absolute; left: 0; width: 100%; top: 632px;
    display: flex; align-items: center; justify-content: center; gap: 10px;
    font-size: 24px; font-weight: 500; color: var(--brand);
  }
  .brand__dot { width: 14px; height: 14px; border-radius: 50%; background: var(--brand); }
</style>
</head>
<body>

<section class="card card--front">
  <svg class="split" width="529" height="794" viewBox="0 0 529 794" aria-hidden="true">
    <defs>
      <linearGradient id="darkMarble" x1="0" y1="0" x2="1" y2="1">
        <stop offset="0" stop-color="#161616"/>
        <stop offset=".5" stop-color="#080808"/>
        <stop offset="1" stop-color="#050505"/>
      </linearGradient>
      <linearGradient id="lightMarble" x1="0" y1="0" x2="1" y2="1">
        <stop offset="0" stop-color="#f6f6f6"/>
        <stop offset=".6" stop-color="#eeeeee"/>
        <stop offset="1" stop-color="#d8d8d8"/>
      </linearGradient>
    </defs>
    <rect width="529" height="794" fill="url(#lightMarble)"/>
    <polygon points="0,0 528,0 0,794" fill="url(#darkMarble)"/>
  </svg>

  <div class="floral-area" role="img" aria-label="Vintage bouquet of ivory and plum roses with sage leaves framing the quote"></div>

  <div class="quote-frame"></div>
  <div class="quote-panel">
    <p class="quote">When the people we love<br>are taken from us,<br>the way to have<br>them live on<br>is to never stop<br>loving them.</p>
  </div>
</section>

<section class="card card--back">
  <div class="notice notice--warning">
    <h2 class="notice__title">WARNING</h2>
    <p class="notice__body">Burn within sight. Keep away from<br>flammable objects. Kep away from<br>children and pets.</p>
  </div>

  <div class="notice notice--burning">
    <h2 class="notice__title">BURNING INSTRUCTIONS</h2>
    <p class="notice__body">Trim wick to 1/4″ before lighting. Keep<br>candle from materials including matches<br>and wick trimmings. Only burn the candle<br>on a level fire resistant surface. Do not<br>burn candle for more than four (4) hours at<br>a time. Stop use when only 1/4″ of wax<br>remains.</p>
  </div>

  <div class="brand">
    <span class="brand__dot"></span>
    <span class="brand__name">Serene Grove</span>
  </div>
</section>

</body>
</html>
```